One page financial canvas needed

I am in the process of developing a financial planning process that uses a one page canvas as a tool for financial education and to explain simple and complex financial strategies to clients. I have the layout and content sorted, just need a hand making it look professional.

It should be a fairly simple project and i have attached a very rough hand drawn canvas showing the desired layout and content. Please feel free to be creative with the design keeping in mind this layout has been chosen to achieve certain outcomes.

Target Market(s)

25-45 Year old Homeowners who are interested in taking better care of the finances

Industry/Entity Type

Financial

Colors

Designer to choose colors to be used in the design.

Requirements
Must have
• very close to the layout in the attached file

```html
<!DOCTYPE html>
<html lang="en">
<head>
<meta charset="utf-8">
<title>Financial Planning Canvas</title>
<link rel="stylesheet" href="https://fonts.googleapis.com/css2?family=Source+Sans+3:wght@400;600&display=swap">
<style>
  :root {
    --panel-blue: #1f67a6;
    --center-white: #f3f4f5;
    --band-grey: #b4bdd0;
    --pill-top: #8ea8e2;
    --pill-bottom: #3a58ad;
    --pill-edge: #2a3d78;
    --icon-blue: #1f67a6;
    --icon-light: #e6edf5;
    --star-dark: #1c1c1c;
    --star-light: #6a6a6a;
    --rule: #3a3a3a;
    --ink-white: #ffffff;
  }
  html, body {
    margin: 0;
    padding: 0;
    width: 1200px;
    height: 858px;
    overflow: hidden;
    background: #ffffff;
  }
  .canvas {
    position: relative;
    width: 1200px;
    height: 858px;
    overflow: hidden;
    font-family: "Source Sans 3", sans-serif;
    background: var(--center-white);
  }
  .panel { position: absolute; top: 0; height: 780px; }
  .panel--left { left: 0; width: 306px; background: var(--panel-blue); }
  .panel--center { left: 306px; width: 588px; background: var(--center-white); }
  .panel--right { left: 894px; width: 306px; background: var(--panel-blue); }
  .band-time {
    position: absolute; left: 0; top: 780px; width: 1200px; height: 78px;
    background: var(--band-grey);
  }

  .pill {
    position: absolute;
    box-sizing: border-box;
    height: 47px;
    border-radius: 20px;
    border: 2px solid var(--pill-edge);
    background: linear-gradient(to bottom, var(--pill-top) 0%, #6f8ed6 40%, var(--pill-bottom) 100%);
    box-shadow: 0 3px 4px rgba(0,0,0,0.35);
    color: var(--ink-white);
    font-size: 36px;
    font-weight: 400;
    line-height: 43px;
    text-align: center;
    letter-spacing: 0.5px;
  }

  .art {
    position: absolute;
    border-radius: 10px;
  }
  .art--on-white { background: var(--icon-blue); }
  .art--on-blue { background: var(--icon-light); }

  .rule { position: absolute; background: var(--rule); }
  .rule--v { width: 1.5px; left: 600px; }
  .rule--h { height: 1.5px; top: 390px; }

  .starburst {
    position: absolute; left: 512px; top: 297px; width: 176px; height: 176px;
  }
  .starburst__point {
    position: absolute; left: 26px; top: 26px; width: 124px; height: 124px;
    background: var(--star-dark);
  }
  .starburst__core {
    position: absolute; left: 12px; top: 12px; width: 152px; height: 152px;
    border-radius: 50%;
    background: radial-gradient(circle at 50% 35%, var(--star-light) 0%, #333 55%, var(--star-dark) 100%);
  }
  .starburst__label {
    position: absolute; left: 0; top: 38px; width: 176px;
    color: var(--ink-white); text-align: center;
    font-size: 39px; line-height: 48px;
  }

  .icon { position: absolute; }
</style>
</head>
<body>
<main class="canvas">
  <section class="panel panel--left"></section>
  <section class="panel panel--center"></section>
  <section class="panel panel--right"></section>
  <footer class="band-time"></footer>

  <!-- Goals -->
  <svg class="icon icon-goals" style="left:10px;top:10px" width="74" height="74" viewBox="0 0 74 74" aria-hidden="true">
    <circle cx="37" cy="37" r="33" fill="none" stroke="#e9ecef" stroke-width="7"/>
    <circle cx="37" cy="37" r="20" fill="none" stroke="#e9ecef" stroke-width="6"/>
    <circle cx="37" cy="37" r="7" fill="#e9ecef"/>
    <path d="M37 37 L52 26" stroke="#e9ecef" stroke-width="3"/>
    <path d="M48 22 L60 24 L52 33 Z" fill="#f08a24"/>
  </svg>
  <div class="pill" style="left:9px;top:92px;width:132px">GOALS</div>

  <!-- Income / Expenses -->
  <div class="art art--on-white" role="img" aria-label="Icon of a hand receiving banknotes" style="left:406px;top:12px;width:110px;height:107px"></div>
  <div class="pill" style="left:350px;top:130px;width:217px">INCOME</div>

  <div class="art art--on-white" role="img" aria-label="Icon of stacked coins with a downward arrow" style="left:702px;top:12px;width:107px;height:107px"></div>
  <div class="pill" style="left:640px;top:130px;width:219px">EXPENSES</div>

  <!-- Cross rules -->
  <div class="rule rule--v" style="top:37px;height:248px"></div>
  <div class="rule rule--v" style="top:482px;height:134px"></div>
  <div class="rule rule--h" style="left:319px;width:191px"></div>
  <div class="rule rule--h" style="left:693px;width:189px"></div>

  <!-- Cash flow starburst -->
  <div class="starburst">
    <div class="starburst__point" style="transform:rotate(0deg)"></div>
    <div class="starburst__point" style="transform:rotate(15deg)"></div>
    <div class="starburst__point" style="transform:rotate(30deg)"></div>
    <div class="starburst__point" style="transform:rotate(45deg)"></div>
    <div class="starburst__point" style="transform:rotate(60deg)"></div>
    <div class="starburst__point" style="transform:rotate(75deg)"></div>
    <div class="starburst__core"></div>
    <div class="starburst__label">CASH<br>FLOW</div>
  </div>

  <!-- Assets / Debt -->
  <div class="art art--on-white" role="img" aria-label="Icon of a padlocked bag holding money sacks" style="left:376px;top:401px;width:74px;height:94px"></div>
  <div class="pill" style="left:329px;top:506px;width:170px">ASSETS</div>

  <div class="art art--on-white" role="img" aria-label="Icon of a figure carrying a heavy money sack" style="left:738px;top:397px;width:97px;height:100px"></div>
  <div class="pill" style="left:705px;top:506px;width:170px">DEBT</div>

  <!-- Wealth -->
  <div class="art art--on-white" role="img" aria-label="Icon of a locked treasure chest" style="left:546px;top:625px;width:109px;height:90px"></div>
  <div class="pill" style="left:515px;top:724px;width:170px">WEALTH</div>

  <!-- Right column -->
  <div class="art art--on-blue" role="img" aria-label="Icon expressing fear" style="left:904px;top:7px;width:75px;height:76px;border-radius:50%"></div>
  <div class="pill" style="left:906px;top:92px;width:130px">FEARS</div>

  <div class="art art--on-blue" role="img" aria-label="Icon of a frustrated person" style="left:908px;top:271px;width:84px;height:85px"></div>
  <div class="pill" style="left:908px;top:363px;width:277px">FRUSTRATIONS</div>

  <div class="art art--on-blue" role="img" aria-label="Icon of a handshake" style="left:908px;top:531px;width:111px;height:72px"></div>
  <div class="pill" style="left:906px;top:616px;width:195px">PARTNERS</div>

  <!-- Time -->
  <svg class="icon icon-clock" style="left:10px;top:784px" width="62" height="62" viewBox="0 0 62 62" aria-hidden="true">
    <circle cx="31" cy="31" r="28" fill="#ffffff" stroke="#111" stroke-width="3"/>
    <g stroke="#111" stroke-width="2">
      <line x1="31" y1="6" x2="31" y2="10"/>
      <line x1="31" y1="52" x2="31" y2="56"/>
      <line x1="6" y1="31" x2="10" y2="31"/>
      <line x1="52" y1="31" x2="56" y2="31"/>
    </g>
    <path d="M31 31 L24 17 M31 31 L44 31" stroke="#111" stroke-width="2.5" fill="none"/>
    <circle cx="31" cy="31" r="2.5" fill="#111"/>
  </svg>
  <div class="pill" style="left:78px;top:791px;width:118px">TIME</div>
</main>
</body>
</html>
```